Landing page design for my current website

I need a landing page designed for my Wordpress website. My website is Lampwicket.com, and I need a page that will serve as a landing page for online ads I run. Please follow the color scheme of the current website

This web page will be targeted towards real estate owners who are looking for a property manager. Above the fold needs to have a CTA form headlined with "As a Rental Property Owner, I Want More Protection, Less Stress, and Drama-Free Living"

A few highlights that can be listed beyond the CTA and fold

- Comprehensive Property Management
Full-service management covering tenant placement, leasing, maintenance, and inspections.

Maximized Rental Income
Proven strategies to optimize rental rates and minimize vacancies, ensuring higher ROI.

Stress-Free Management
We handle all tenant interactions, maintenance requests, and property issues, so you don't have to.

Experienced Team
Over a decade of experience in managing single-family homes, small multifamily units, and apartment complexes.

Advanced Technology
Utilize cutting-edge property management software for efficient communication, rent collection, and maintenance tracking.

Tenant Screening and Placement
Thorough background checks and tenant screening processes to ensure reliable and responsible tenants.

Regular Property Inspections
Routine inspections to maintain property condition and address issues before they become costly problems.

Legal Compliance
Expertise in local and federal rental laws to keep your properties compliant and avoid legal hassles.

Transparent Reporting
Detailed monthly reports and financial statements to keep you informed about your property's performance.

Personalized Service
Tailored management plans to meet the unique needs of your properties and investment goals.
Effective Tenant Conflict Resolution
Skilled in handling challenging tenant situations, ensuring conflicts are resolved quickly and professionally to maintain a peaceful living environment and protect your investment.

```html
<!DOCTYPE html>
<html lang="en">
<head>
<meta charset="utf-8">
<title>Lampwicket Realty – Property Management</title>
<link href="https://fonts.googleapis.com/css2?family=Oswald:wght@400;500&family=Lexend:wght@400;500&family=Nunito+Sans:wght@400;600;700&display=swap" rel="stylesheet">
<style>
:root{
  --navy:#123f78;
  --navy-deep:#0c2f5c;
  --arc-dark:#1a2433;
  --grey-bg:#f5f5f5;
  --text:#333a44;
  --line:#d9dde3;
  --white:#ffffff;
}
*{box-sizing:border-box;margin:0;padding:0}
html,body{width:1200px;height:3588px;overflow:hidden}
body{position:relative;font-family:"Nunito Sans",sans-serif;color:var(--text);background:var(--white)}
.section{position:absolute;left:0;width:1200px}
.abs{position:absolute}
.btn{position:absolute;display:flex;align-items:center;justify-content:center;background:var(--navy);color:var(--white);font:600 14px "Nunito Sans",sans-serif;border-radius:24px;height:44px;width:132px}
.brand{display:flex;align-items:center;gap:10px;font:500 20px "Lexend",sans-serif;color:var(--navy)}
.brand .dot{width:34px;height:34px;border-radius:50%;border:3px solid var(--navy)}
.heading{font:500 38px "Lexend",sans-serif;color:var(--navy);text-align:center;position:absolute;left:0;width:1200px}
.rule{position:absolute;height:3px;width:76px;background:var(--navy);left:562px}

/* hero */
.hero{top:0;height:546px}
.hero-title{left:163px;top:205px;font:400 39px/47px "Oswald",sans-serif;color:#1e2430;width:360px}
.call{left:740px;top:24px;display:flex;gap:10px;align-items:center;color:var(--white)}
.call small{display:block;font-size:13px}
.call b{font-weight:600;font-size:17px}
.top-btn{left:903px;top:21px;background:var(--white);color:var(--navy);height:44px;width:133px}
.photo-circle{left:584px;top:132px;width:418px;height:418px;border-radius:50%;background:linear-gradient(150deg,#8b9fb6,#4d6e93 55%,#6d8c6a)}
.badge{left:883px;top:450px;width:116px;height:116px;border-radius:50%;background:var(--navy);border:3px solid var(--white);color:var(--white);font:400 16px/19px "Oswald",sans-serif;text-align:center;display:flex;align-items:center;justify-content:center}

/* benefits */
.benefits{top:546px;height:916px;background:var(--grey-bg)}
.orbit{left:345px;top:191px;width:488px;height:488px;border-radius:50%;border:1.5px solid #e2e4e8}
.core{left:450px;top:296px;width:278px;height:278px;border-radius:50%;background:var(--white);box-shadow:0 6px 28px rgba(0,0,0,.12);display:flex;align-items:center;justify-content:center;font:500 30px "Lexend",sans-serif;color:var(--navy);text-align:center}
.node{position:absolute;width:86px;height:86px;margin:-43px 0 0 -43px;border-radius:50%;background:var(--white);border:3px solid var(--navy)}
.label{position:absolute;font:600 13.5px/19px "Nunito Sans",sans-serif;color:#1e2430}
.label.r{text-align:right}

/* why */
.why{top:1462px;height:619px}
.why-copy{left:159px;top:178px;width:420px;font-size:12.7px;line-height:22px}
.why-copy p{margin-bottom:9px}
.checks{list-style:none}
.checks li{display:flex;align-items:center;gap:9px;line-height:24.5px}
.house-photo{left:612px;top:175px;width:424px;height:337px;border-radius:6px;background:linear-gradient(180deg,#5f7f5a 0%,#4b5c78 35%,#3f4d66 65%,#5d8a3f 100%);box-shadow:6px -4px 0 #c9d8ea}

/* reviews */
.reviews{top:2081px;height:525px;background:var(--grey-bg)}
.sub{left:0;width:1200px;top:152px;text-align:center;font-size:13px;line-height:23px}
.card{position:absolute;top:213px;width:269px;height:223px;background:var(--white);border:1px solid var(--line);border-radius:3px;padding:20px 9px 0 9px;font-size:12.7px;line-height:23px}
.card .who{position:absolute;left:9px;right:9px;bottom:14px;border-top:1px solid var(--line);padding-top:12px;display:flex;align-items:center;gap:10px}
.avatar{width:34px;height:34px;border-radius:50%;color:var(--white);font:600 20px "Nunito Sans",sans-serif;display:flex;align-items:center;justify-content:center}
.who span{font-size:12px;line-height:17px}
.mark{margin-left:auto;width:46px;height:14px;border-radius:3px;background:#dfe5ee}
.arrow{position:absolute;top:317px}

/* about */
.about{top:2606px;height:700px}
.about h2{position:absolute;left:163px;top:112px;font:500 38px "Lexend",sans-serif;color:var(--navy)}
.about-copy{left:162px;top:190px;width:482px;font-size:12.7px;line-height:23.5px}
.about-copy p{margin-bottom:7px}
.about-copy a{color:var(--navy);font-weight:600;text-decoration:none}
.contact-item{position:absolute;left:160px;display:flex;gap:14px;align-items:center;color:var(--navy);font-size:18px;line-height:21px}
.faint{left:458px;top:425px;font:500 32px "Lexend",sans-serif;color:#ebedf0}
.form{left:707px;top:89px;width:330px;height:454px;background:var(--navy);border-radius:6px;padding:26px 17px 0}
.form h3{font:400 24px "Oswald",sans-serif;color:var(--white);text-align:center}
.form .rl{height:1px;background:#4e72a0;margin:10px 0 50px}
.field{background:var(--white);height:39px;border-radius:2px;margin-bottom:8px;padding:11px 11px;font-size:13px;color:#777;position:relative}
.field b{color:#d22}
.field.tall{height:78px}
.submit{background:#cfd3d9;height:39px;margin-top:20px;border-radius:2px;display:flex;align-items:center;justify-content:center;color:var(--navy);font-weight:700;font-size:15px}

/* footer */
.footer{top:3260px;height:328px}
.foot-logo{left:536px;top:-4px;width:126px;height:126px;border-radius:50%;background:var(--white);display:flex;align-items:center;justify-content:center;font:500 16px/20px "Lexend",sans-serif;color:var(--navy);text-align:center}
.foot-name{left:0;width:1200px;top:138px;text-align:center;color:var(--white);font:500 26px "Lexend",sans-serif}
.foot-text{left:190px;width:820px;top:185px;text-align:center;color:var(--white);font-size:13px;line-height:24px}
.foot-rule{left:162px;width:876px;top:259px;height:1px;background:#3d6497}
.foot-bottom{left:162px;width:876px;top:275px;display:flex;justify-content:space-between;color:var(--white);font-size:12.5px}
</style>
</head>
<body>

<section class="section hero">
  <svg class="abs" style="left:0;top:0" width="1200" height="546" role="img" aria-label="Evening photo of a modern two-storey house under a navy tint">
    <defs><linearGradient id="houseTint" x1="0" y1="0" x2="1" y2="1"><stop offset="0" stop-color="#2b4a7c"/><stop offset="1" stop-color="#173b6e"/></linearGradient></defs>
    <path d="M470 0H1200V435C1070 440 935 395 820 310C690 215 520 130 470 0Z" fill="url(#houseTint)"/>
  </svg>
  <div class="abs brand" style="left:163px;top:22px"><span class="dot"></span>LAMPWICKET REALTY</div>
  <div class="abs call">
    <svg width="28" height="28" viewBox="0 0 24 24" fill="none" stroke="#fff" stroke-width="1.5"><path d="M5 3h4l2 5-2.5 1.5a11 11 0 0 0 6 6L16 13l5 2v4a2 2 0 0 1-2 2A17 17 0 0 1 3 5a2 2 0 0 1 2-2z"/></svg>
    <div><small>Call or Text</small><b>555.014.2290</b></div>
  </div>
  <div class="btn top-btn">Get In Touch</div>
  <h1 class="abs hero-title">As a Rental Property Owner, I Want More Protection, Less Stress, and Drama-Free Living</h1>
  <div class="btn" style="left:161px;top:413px">Get In Touch</div>
  <div class="abs photo-circle" role="img" aria-label="Photo of a property manager in a suit greeting a smiling homeowner outside a house"></div>
  <div class="abs badge">Providing<br>Homes &amp;<br>Apartments<br>for Rent</div>
</section>

<section class="section benefits">
  <h2 class="heading" style="top:80px">Benefits You Get</h2>
  <div class="rule" style="top:134px"></div>
  <div class="abs orbit"></div>
  <div class="abs core">Lampwicket<br>Realty</div>

  <div class="node" style="left:486px;top:227px"></div>
  <div class="node" style="left:636px;top:207px"></div>
  <div class="node" style="left:768px;top:277px"></div>
  <div class="node" style="left:834px;top:405px"></div>
  <div class="node" style="left:813px;top:551px"></div>
  <div class="node" style="left:717px;top:657px"></div>
  <div class="node" style="left:557px;top:687px"></div>
  <div class="node" style="left:419px;top:618px"></div>
  <div class="node" style="left:351px;top:485px"></div>
  <div class="node" style="left:377px;top:331px"></div>

  <div class="label r" style="right:776px;top:201px">Effective Tenant<br>Conflict Resolution</div>
  <div class="label" style="left:692px;top:177px">Comprehensive Property<br>Management</div>
  <div class="label" style="left:831px;top:259px">Maximized<br>Rental Income</div>
  <div class="label" style="left:895px;top:387px">Stress-Free<br>Management</div>
  <div class="label" style="left:874px;top:532px">Tenant Screening And<br>Placement</div>
  <div class="label" style="left:780px;top:651px">Experienced Team And<br>Personalized Service</div>
  <div class="label r" style="right:702px;top:700px">Advanced Technology</div>
  <div class="label r" style="right:841px;top:608px">Legal Compliance</div>
  <div class="label r" style="right:910px;top:466px">Transparent<br>Reporting</div>
  <div class="label r" style="right:884px;top:314px">Regular<br>Property Inspections</div>

  <div class="btn" style="left:521px;top:782px">Get In Touch</div>
</section>

<section class="section why">
  <h2 class="heading" style="top:90px">Why “Lampwicket Realty”</h2>
  <div class="rule" style="top:144px"></div>
  <div class="abs why-copy">
    <p>Lampwicket refers to tenants as residents – providing an excellence experience to residents is our number 1 mission followed by leading our clients towards true wealth building.</p>
    <p>When investors partner with Lampwicket Realty property management our partnership focuses on providing a resident first experience. In this case, we have Lampwicket Tenants, only residents.</p>
    <ul class="checks">
      <li><svg width="15" height="10" viewBox="0 0 15 10" fill="none" stroke="#123f78" stroke-width="2"><path d="M1 9C4 4 8 3 13 3M10 1l3 2-3 2"/></svg>Excellent Tenant Care &amp; True Tenant Screening</li>
      <li><svg width="15" height="10" viewBox="0 0 15 10" fill="none" stroke="#123f78" stroke-width="2"><path d="M1 9C4 4 8 3 13 3M10 1l3 2-3 2"/></svg>Easy Move In &amp; Move Out Process</li>
      <li><svg width="15" height="10" viewBox="0 0 15 10" fill="none" stroke="#123f78" stroke-width="2"><path d="M1 9C4 4 8 3 13 3M10 1l3 2-3 2"/></svg>Flexible Leasing Options</li>
      <li><svg width="15" height="10" viewBox="0 0 15 10" fill="none" stroke="#123f78" stroke-width="2"><path d="M1 9C4 4 8 3 13 3M10 1l3 2-3 2"/></svg>First Responder Benefits &amp; Also Hearthline Benefits</li>
      <li><svg width="15" height="10" viewBox="0 0 15 10" fill="none" stroke="#123f78" stroke-width="2"><path d="M1 9C4 4 8 3 13 3M10 1l3 2-3 2"/></svg>5 Star Property Management</li>
      <li><svg width="15" height="10" viewBox="0 0 15 10" fill="none" stroke="#123f78" stroke-width="2"><path d="M1 9C4 4 8 3 13 3M10 1l3 2-3 2"/></svg>All Utilities Included</li>
    </ul>
  </div>
  <div class="abs house-photo" role="img" aria-label="Photo of a navy craftsman-style house with stone porch and green lawn"></div>
  <div class="btn" style="left:161px;top:484px">Get In Touch</div>
</section>

<section class="section reviews">
  <h2 class="heading" style="top:88px">Residents Love Lampwicket, Inc.</h2>
  <div class="rule" style="top:142px"></div>
  <p class="abs sub">Residents that rent houses and apartments from Lampwicket quickly fall in-love with the over-attention to detail and resident care.<br>It's Lampwicket's goal to promote a safe and affordable way of living. Just read for yourself!</p>
  <svg class="arrow" style="left:118px" width="28" height="14" viewBox="0 0 28 14" fill="none" stroke="#999" stroke-width="2"><path d="M27 7H2M8 1L2 7l6 6"/></svg>
  <div class="card" style="left:161px">100% recommended the contractor gives a good service very friendly gives a detailed explanation of the place and the super clean place I was fascinated by the place.
    <div class="who"><div class="avatar" style="background:#2e8b57">M</div><span>Marco Rivas<br>1 month ago</span><i class="mark"></i></div></div>
  <div class="card" style="left:465px">I loved the staff, the quality of the things, the good service, the punctuality, the location of the apartment, super recommended and super delighted with the result.
    <div class="who"><div class="avatar" style="background:#f57c00">D</div><span>Delia Fontaine<br>1 month ago</span><i class="mark"></i></div></div>
  <div class="card" style="left:768px">Everything has been going really great, I haven't had any issues with the property we live on, very clean. Communication with our land landlord John is always fast and beneficial!
    <div class="who"><div class="avatar" style="background:#b35a12">R</div><span>Renata<br>1 month ago</span><i class="mark"></i></div></div>
  <svg class="arrow" style="left:1056px" width="28" height="14" viewBox="0 0 28 14" fill="none" stroke="#123f78" stroke-width="2.5"><path d="M1 7h25M20 1l6 6-6 6"/></svg>
</section>

<section class="section about">
  <h2>About Us</h2>
  <div class="abs about-copy">
    <p>Lampwicket, Inc. offers affordable, safe, up-to-date housing options in the Alder Falls, Brookhaven, and Westmere Pennsylvania markets. <a>Contact us today if you're looking for your next rental.</a></p>
    <p>When Partnered with Lampwicket you'll have access to specialty Realty rates. If you use our team as a property manager you'll enjoy discounted rates for selling properties through our Real Estate office. <a>Contact our team to learn more about this network perk.</a></p>
  </div>
  <div class="abs faint">Lampwicket</div>
  <div class="contact-item" style="top:378px">
    <svg width="38" height="38" viewBox="0 0 24 24" fill="none" stroke="#123f78" stroke-width="1.3"><path d="M5 3h4l2 5-2.5 1.5a11 11 0 0 0 6 6L16 13l5 2v4a2 2 0 0 1-2 2A17 17 0 0 1 3 5a2 2 0 0 1 2-2z"/></svg>
    <div>Phone<br>555.014.2290</div>
  </div>
  <div class="contact-item" style="top:437px">
    <svg width="38" height="38" viewBox="0 0 24 24" fill="none" stroke="#123f78" stroke-width="1.3"><rect x="2" y="6" width="20" height="15"/><path d="M2 6l10 8 10-8M2 21l8-7M22 21l-8-7"/></svg>
    <div>Email<br>Hello@lampwicket.com</div>
  </div>
  <div class="btn" style="left:160px;top:497px">Get In Touch</div>

  <form class="abs form">
    <h3>Contact Lampwicket Realty</h3>
    <div class="rl"></div>
    <div class="field" style="margin-top:-36px">Name<b>*</b></div>
    <div class="field">Phone<b>*</b></div>
    <div class="field">Email<b>*</b></div>
    <div class="field">Inquiry For<b>*</b><svg style="position:absolute;right:12px;top:15px" width="10" height="6" viewBox="0 0 10 6" fill="none" stroke="#777"><path d="M1 5l4-4 4 4"/></svg></div>
    <div class="field tall">Message<b>*</b></div>
    <div class="submit">Submit Now</div>
  </form>
</section>

<section class="section footer">
  <svg class="abs" style="left:0;top:0" width="1200" height="328">
    <path d="M0 200C300 44 900 44 1200 200V328H0Z" fill="var(--arc-dark)"/>
    <path d="M0 215C300 60 900 60 1200 215V328H0Z" fill="var(--navy)"/>
  </svg>
  <div class="abs foot-logo">Lampwicket<br>Realty</div>
  <div class="abs foot-name">Lampwicket Realty</div>
  <p class="abs foot-text">At Lampwicket Realty, we measure our achievements not just in terms of leases signed but by the smiles and satisfaction of our community members.</p>
  <div class="abs foot-rule"></div>
  <div class="abs foot-bottom">
    <span>© 2024. Lampwicket Realty. All Rights Reserved</span>
    <span style="display:flex;gap:8px;align-items:center"><svg width="14" height="18" viewBox="0 0 14 18" fill="none" stroke="#fff" stroke-width="1.4"><path d="M7 17s6-6 6-10A6 6 0 0 0 1 7c0 4 6 10 6 10z"/><circle cx="7" cy="7" r="2.2"/></svg>118 Orchard Lane Millbrook PA, 17900</span>
  </div>
</section>

</body>
</html>
```